Plakat-Design für Förderverein einer Feuerwehr
Zielgruppe
Wir sind ein Förderverein einer Feuerwehr und suchen ein modernes Design für unser Banner und Plakat für das Maifest
Aufgabenstellung
Das Banner soll die Maße von 2x1m haben und das Plakat soll das Format A3 haben. Der Textinhalt soll so bleiben.

```html
<!DOCTYPE html>
<html lang="de">
<head>
<meta charset="utf-8">
<title>Maifest Feuerwehr – Plakat und Banner</title>
<link rel="stylesheet" href="https://fonts.googleapis.com/css2?family=Barlow+Condensed:ital,wght@1,600;1,800&display=swap">
<style>
  :root {
    --paper: #ffffff;
    --ink: #15181a;
    --white: #ffffff;
    --sky: #8fb8d8;
    --haze: #f6eef5;
    --cylinder: #e3cf2a;
    --coat: #1c2226;
    --night: #0b0d0c;
    --olive: #6f8a2a;
    --moss: #3f4f24;
    --amber: #a89030;
  }
  * { box-sizing: border-box; margin: 0; padding: 0; }
  html, body { width: 884px; height: 1200px; overflow: hidden; background: var(--paper); }
  body { position: relative; font-family: "Barlow Condensed", "Arial Narrow", sans-serif; font-style: italic; }

  .poster { position: absolute; left: 108px; top: 92px; width: 419px; height: 569px; overflow: hidden; }
  .banner { position: absolute; left: 108px; top: 736px; width: 667px; height: 320px; overflow: hidden; }

  .photo {
    position: absolute;
    background:
      radial-gradient(ellipse 30% 45% at 52% 62%, var(--cylinder) 0 45%, transparent 70%),
      radial-gradient(ellipse 40% 50% at 85% 70%, var(--coat) 0 50%, transparent 80%),
      radial-gradient(ellipse 35% 40% at 30% 85%, var(--coat) 0 50%, transparent 80%),
      linear-gradient(160deg, var(--sky) 0%, var(--haze) 35%, var(--haze) 55%, #9aa0a4 100%);
  }
  .poster .photo { left: 0; top: 0; width: 419px; height: 297px; }
  .banner .photo { left: 0; top: 0; width: 334px; height: 320px; }

  .glow {
    position: absolute;
    background:
      radial-gradient(ellipse 40% 30% at 30% 10%, rgba(168,144,48,.55), transparent 70%),
      radial-gradient(ellipse 35% 30% at 75% 45%, rgba(111,138,42,.7), transparent 70%),
      radial-gradient(ellipse 50% 30% at 60% 95%, rgba(111,138,42,.9), transparent 75%),
      radial-gradient(ellipse 30% 25% at 15% 55%, rgba(63,79,36,.8), transparent 75%),
      var(--night);
  }
  .poster .glow { left: 0; top: 297px; width: 419px; height: 272px; }
  .banner .glow {
    left: 334px; top: 0; width: 333px; height: 320px;
    background:
      radial-gradient(ellipse 35% 25% at 65% 5%, rgba(168,144,48,.85), transparent 70%),
      radial-gradient(ellipse 30% 40% at 100% 60%, rgba(150,170,60,.85), transparent 70%),
      radial-gradient(ellipse 50% 30% at 40% 100%, rgba(111,138,42,.8), transparent 75%),
      radial-gradient(ellipse 25% 40% at 0% 20%, rgba(150,150,150,.6), transparent 70%),
      #1d241f;
  }

  .headline { position: absolute; color: var(--ink); font-weight: 800; text-transform: uppercase; }
  .headline .title { font-size: 43px; line-height: .82; letter-spacing: -1px; }
  .headline .club { font-size: 12.5px; line-height: .95; font-weight: 800; margin-top: 4px; }
  .poster .headline { left: 20px; top: 22px; }
  .banner .headline { left: 29px; top: 28px; }
  .banner .headline .title { font-size: 40px; }

  .club-mark { position: absolute; display: flex; align-items: center; gap: 5px; font-weight: 800; text-transform: uppercase; font-size: 12px; }
  .club-mark .dot { width: 14px; height: 14px; border-radius: 50%; }
  .poster .club-mark { right: 18px; top: 40px; color: var(--ink); }
  .poster .club-mark .dot { background: var(--ink); }
  .banner .club-mark { left: 370px; top: 55px; color: var(--white); font-size: 16px; }
  .banner .club-mark .dot { background: var(--white); width: 18px; height: 18px; }

  .info { position: absolute; color: var(--white); font-weight: 800; text-transform: uppercase; }
  .poster .program { left: 30px; top: 345px; font-size: 18.5px; line-height: .92; }
  .poster .program p + p { margin-top: 12px; }
  .poster .extras { right: 31px; top: 488px; font-size: 12.5px; line-height: .98; text-align: right; }
  .date { position: absolute; color: var(--white); font-weight: 800; letter-spacing: -1px; }
  .poster .date { right: 31px; top: 505px; font-size: 56px; line-height: 1; }

  .banner .time { left: 372px; top: 133px; font-size: 22px; }
  .banner .program { left: 369px; top: 172px; font-size: 17px; line-height: .95; }
  .banner .date { left: 368px; top: 230px; font-size: 48px; line-height: 1; }
</style>
</head>
<body>
  <section class="poster">
    <div class="photo" role="img" aria-label="Foto: Feuerwehrleute mit Helm und gelben Atemschutzflaschen vor hellem Himmel"></div>
    <div class="glow"></div>
    <div class="headline">
      <div class="title">Maifest<br>Feuerwehr<br>Bad Lindental</div>
      <div class="club">Förderverein der FF<br>Löschzug Eichenberg e.V.</div>
    </div>
    <div class="club-mark"><span class="dot"></span>FV Lindental</div>
    <div class="info program">
      <p>Ab 12:00 Uhr: Tag der offenen Tür</p>
      <p>Den ganzen Tag:<br>Softdrinks, Bier vom Fass &amp;<br>Spezialitäten vom Grill</p>
    </div>
    <div class="info extras">Ausstellung der Fahrzeuge<br>Belustigung der Kleinen, mit Hüpfburg</div>
    <div class="date">26. MAI 2024</div>
  </section>

  <section class="banner">
    <div class="photo" role="img" aria-label="Foto: Feuerwehrleute mit Helm und gelben Atemschutzflaschen vor hellem Himmel"></div>
    <div class="glow"></div>
    <div class="headline">
      <div class="title">Maifest<br>Feuerwehr<br>Bad Lindental</div>
      <div class="club">Förderverein der FF<br>Löschzug Eichenberg e.V.</div>
    </div>
    <div class="club-mark"><span class="dot"></span>FV Lindental</div>
    <div class="info time">Ab 12:00 Uhr</div>
    <div class="info program">Tag der offenen Tür,<br>Softdrinks, Bier vom Fass &amp;<br>Spezialitäten vom Grill</div>
    <div class="date">26. MAI 2024</div>
  </section>
</body>
</html>
```